Design a wedding invitation

I need a classic and beautiful wedding invitation design URGENTLY
I have uploaded some example invitations where I like the LAYOUT only - PLESE REFER TO THIS LAYOUT FOR IMAGE, LOGO AND TEXT !
The imagery is in the other file uploaded - there are two options for the imagery whichever one works best with the layout
I would like to include some sort of logo of our initials H&L if possible
Size is A5
I would like to keep the same colour palette as the artworks
I do not want to make the Vantrel Arch the centre of the design we are looking for a more subtle effect
We want to avoid the look of 'image at the bottom and text at the top' by creating one unified piece
The final design will be letterpress printed with embossing so image cannot overlap with text
The wording is as follows:

“The honour of your presence
is requested at the wedding of Lucinda Marsh to Henrik Dalvang
Saturday, the eighth of September Two thousand and eighteen
at six o’clock in the evening
Château du Q
Paris, France
Black Tie"

```html
<!DOCTYPE html>
<html lang="en">
<head>
<meta charset="utf-8">
<title>Lucinda &amp; Henrik – Wedding Invitation</title>
<link rel="stylesheet" href="https://fonts.googleapis.com/css2?family=Italianno&family=Tinos&display=swap">
<style>
  :root {
    --backdrop: #1c1c1e;
    --card: #ffffff;
    --ink: #1a1a1a;
    --accent-red: #c0262c;
    --blossom: #e8b9c4;
    --blossom-deep: #c98a9e;
    --sky: #c9d3e6;
    --bark: #6b5a57;
  }
  * { margin: 0; padding: 0; box-sizing: border-box; }
  html, body { width: 1200px; height: 715px; overflow: hidden; }
  body { background: var(--backdrop); position: relative; }

  .invitation {
    position: absolute;
    top: 47px;
    width: 391px;
    height: 604px;
    background: var(--card);
    overflow: hidden;
  }
  .invitation--left { left: 169px; }
  .invitation--right { left: 636px; }

  .invitation__artwork {
    position: absolute;
    inset: 0;
  }
  .invitation--left .invitation__artwork {
    background:
      radial-gradient(ellipse 62% 52% at 67% 38%, var(--card) 45%, rgba(255,255,255,0) 78%),
      linear-gradient(180deg, var(--blossom) 0%, var(--sky) 45%, var(--blossom-deep) 78%, var(--bark) 100%);
  }
  .invitation--right .invitation__artwork {
    background:
      radial-gradient(ellipse 62% 52% at 33% 38%, var(--card) 45%, rgba(255,255,255,0) 78%),
      linear-gradient(180deg, var(--blossom) 0%, var(--sky) 45%, var(--blossom-deep) 78%, var(--bark) 100%);
  }

  .invitation__text {
    position: absolute;
    top: 0;
    width: 230px;
    text-align: center;
    color: var(--ink);
    font-family: "Tinos", "Times New Roman", serif;
  }
  .invitation--left .invitation__text { left: 148px; }
  .invitation--right .invitation__text { left: 11px; }

  .monogram {
    position: absolute;
    top: 16px;
    left: 0; right: 0;
    font-family: "Italianno", cursive;
    font-size: 50px;
    line-height: 1;
    color: var(--ink);
  }

  .line {
    position: absolute;
    left: 0; right: 0;
    font-size: 12px;
    line-height: 1;
    white-space: nowrap;
  }
  .names {
    position: absolute;
    left: 0; right: 0;
    font-family: "Italianno", cursive;
    font-size: 40px;
    line-height: 1;
    color: var(--accent-red);
    white-space: nowrap;
  }
</style>
</head>
<body>

  <article class="invitation invitation--left">
    <div class="invitation__artwork" role="img" aria-label="Watercolour painting of blossoming pink trees along the left edge and a Paris riverside scene with the Vantrel Arch, a street lamp and a strolling couple along the bottom"></div>
    <div class="invitation__text">
      <div class="monogram">H&amp;L</div>
      <p class="line" style="top:86px">The honour of your presence</p>
      <p class="line" style="top:105px">is requested at the wedding of</p>
      <p class="names" style="top:130px">Lucinda Marsh</p>
      <p class="names" style="top:164px">to</p>
      <p class="names" style="top:196px">Henrik Dalvang</p>
      <p class="line" style="top:242px">Saturday, the eighth of September Two</p>
      <p class="line" style="top:264px">thousand and eighteen</p>
      <p class="line" style="top:287px">at six o’clock in the evening</p>
      <p class="line" style="top:310px">Château du Q</p>
      <p class="line" style="top:333px">Paris, France</p>
      <p class="line" style="top:356px">Black Tie</p>
    </div>
  </article>

  <article class="invitation invitation--right">
    <div class="invitation__artwork" role="img" aria-label="Watercolour painting of blossoming pink trees along the right edge and a Paris riverside scene with the Vantrel Arch, a street lamp and a strolling couple along the bottom"></div>
    <div class="invitation__text">
      <div class="monogram">H&amp;L</div>
      <p class="line" style="top:86px">The honour of your presence</p>
      <p class="line" style="top:105px">is requested at the wedding of</p>
      <p class="names" style="top:130px">Lucinda Marsh</p>
      <p class="names" style="top:164px">to</p>
      <p class="names" style="top:196px">Henrik Dalvang</p>
      <p class="line" style="top:242px">Saturday, the eighth of September Two</p>
      <p class="line" style="top:264px">thousand and eighteen</p>
      <p class="line" style="top:287px">at six o’clock in the evening</p>
      <p class="line" style="top:310px">Château du Q</p>
      <p class="line" style="top:333px">Paris, France</p>
      <p class="line" style="top:356px">Black Tie</p>
    </div>
  </article>

</body>
</html>
```